Float and wellness centre needs a website refresh

Our float and wellness centre has been operating in Brisbane, Australia for 3 months. Our website is functional and easy to use, but it lacks a compelling visual experience that sells our awesome services to our customers.<br/><br/>We would like a complete redesign of our webpage. It is very important that the redesign considers the page layout for mobile users and the winning design will need to show both a desktop and mobile version of each of the pages listed below.<br/><br/>Out current website can be found at https://www.ebbtidehaven.com.au/<br/><br/>The winning design will need to provide proposals for redesigning the 4 pages listed below:<br/>Home Page - https://www.ebbtidehaven.com.au/<br/>Float Page - https://www.ebbtidehaven.com.au/services/float<br/>Build Gift Card page - https://www.ebbtidehaven.com.au/giftcard/stepone?location=kelsworth<br/>Booking Page - https://www.ebbtidehaven.com.au/Calendar/Day?centerId=kelsworth&selectedCategory=FLOAT&date=12/18/2019%2000:00:00%20+10:00&sessionLength=60<br/><br/>We only need the 4 pages listed above as our web developer will use the assets from the above pages to standardize all the other pages in the site. It is very important your proposed pages contain the same information as our current pages so that we can properly see the complete layout.<br/><br/>The Home page must display the business logo in some way. We would like the website to have a white background and for it make tasteful use of color to highlight key features on the pages. Where color is used it should harmonize with the business logo. The website needs to feel bright, simple and relaxing. Our current site does not use images very well and we have had professional photos taken of the center and the float rooms specifically for this website project. You can download these, and the business logo images here: http://ebbtidehaven.com.au/websiteimages.zip <br/><br/>We have included a few links below to other centers who have pages that we like: <br/><br/>https://www.drifthollowpods.com/ <br/>https://www.quietnook.com.au/ <br/>https://www.moonbaysoak.com.au/<br/>

Industry/Entity Type

Health And Wellness

Number of Pages Required

4 page

Font styles to use
Sans Serif

Colors

Designer to choose colors to be used in the design.

Requirements
Must have
• It is very important your proposed pages contain the same information as our current pages so that we can properly see the complete layout.
• The Home page must display the business logo in some way.
• Where color is used it should harmonize with the business logo.
Nice to have
• The website needs to feel bright, simple and relaxing. Our current site does not use images very well and we have had professional photos taken of the center and the float rooms specifically for this website project. You can download these, and the business logo images here: http://ebbtidehaven.com.au/websiteimages.zip
Should not have
• Dark pages.

```html
<!DOCTYPE html>
<html lang="en">
<head>
<meta charset="utf-8">
<title>Ebbtide Haven – Float &amp; Wellness</title>
<link href="https://fonts.googleapis.com/css2?family=Nunito+Sans:wght@400;600;700;800&display=swap" rel="stylesheet">
<style>
:root{
  --ink:#111;
  --muted:#555;
  --coral:#f2685a;
  --blush:#fdf3f6;
  --blush-text:#f1b8c8;
  --footer:#f0f0f3;
  --mental:#9b4f9e;
  --physical:#6b72c0;
  --creative:#f2685a;
  --line:#d9d9de;
  --leaf-pink:#fbe3ea;
  --leaf-lilac:#ecebf7;
}
*{margin:0;padding:0;box-sizing:border-box}
html,body{width:1200px;height:2873px;overflow:hidden;background:#fff}
body{position:relative;font-family:"Nunito Sans",Arial,sans-serif;color:var(--ink)}
.abs{position:absolute}
.photo{position:absolute;border:4px solid #fff;box-shadow:0 3px 10px rgba(0,0,0,.18)}

.site-header{position:absolute;left:0;top:0;width:1200px;height:77px;background:#fff}
.brand{position:absolute;display:flex;align-items:center;gap:10px;font-weight:700;color:#222}
.brand-dot{width:30px;height:30px;border-radius:50%;background:var(--coral)}
.main-nav{position:absolute;left:416px;top:31px;display:flex;gap:23px;font-size:11px;font-weight:600}
.btn-book{position:absolute;left:872px;top:23px;width:118px;height:30px;border-radius:15px;background:var(--coral);color:#fff;font-size:8.5px;font-weight:700;letter-spacing:.3px;display:flex;align-items:center;justify-content:center}

.hero{position:absolute;left:0;top:77px;width:1200px;height:488px;background:linear-gradient(100deg,#e9c4a8 0%,#c46a3c 35%,#a8512b 70%,#8d3e1d 100%)}
.blush-band{position:absolute;left:0;top:565px;width:1200px;height:440px;background:var(--blush);clip-path:polygon(0 0,100% 0,100% 96%,0 86%)}
.logo-badge{position:absolute;left:535px;top:510px;width:130px;height:130px;border-radius:50%;background:#fff;box-shadow:0 4px 14px rgba(0,0,0,.12);display:flex;align-items:center;justify-content:center;text-align:center;font-size:15px;font-weight:700;color:#c9436b;line-height:1.2}
.leaf-area{position:absolute;border-radius:50%}

.service .eyebrow{font-size:13px;color:var(--blush-text);font-weight:600}
.service h2{font-size:19px;font-weight:800;margin-top:4px;letter-spacing:.3px}
.service p{font-size:12.5px;line-height:16px;margin-top:8px;font-weight:600;color:#222}
.btn-dark{display:flex;align-items:center;justify-content:center;width:103px;height:31px;background:#000;color:#fff;font-size:8px;font-weight:800;letter-spacing:1.3px;margin-top:24px}

.benefits-title{left:0;top:1333px;width:1200px;text-align:center;font-size:20px;font-weight:700}
.benefit{position:absolute;width:200px;text-align:center}
.benefit .disc{width:104px;height:104px;border-radius:50%;margin:0 auto;display:flex;align-items:center;justify-content:center}
.benefit h3{font-size:16px;font-weight:800;margin-top:20px}
.benefit p{font-size:9.5px;line-height:13px;margin:24px auto 0;width:190px;color:#333}

.water{position:absolute;left:0;top:1661px;width:1200px;height:333px;background:linear-gradient(180deg,#fff 0%,#cfe1ec 35%,#7fa9c6 70%,#5f8fb6 100%)}
.booking-card{position:absolute;left:317px;top:1859px;width:566px;height:336px;background:#fff;box-shadow:0 2px 10px rgba(0,0,0,.06);text-align:center}
.booking-card h2{font-size:16px;font-weight:600;margin-top:37px}
.booking-card .lead{font-size:10.5px;line-height:15px;margin:5px auto 0;width:340px;color:#333}
.field{position:absolute;border:1px solid var(--line);font-size:8.5px;color:#aaa;padding:9px 6px;text-align:left}
.btn-submit{position:absolute;left:243px;top:273px;width:99px;height:29px;background:var(--coral);color:#fff;font-size:9px;font-weight:700;letter-spacing:.8px;display:flex;align-items:center;justify-content:center}

.follow-line{position:absolute;top:2253px;height:1px;background:#222}
.follow-label{left:0;top:2246px;width:1200px;text-align:center;font-size:8.5px;font-weight:800;letter-spacing:1.6px}
.feed-tile{position:absolute;top:2290px;width:196px;height:159px}

.mission{left:322px;top:2484px;width:556px;text-align:center}
.mission .dot{width:38px;height:38px;border-radius:50%;background:var(--coral);margin:0 auto}
.mission h2{font-size:16px;font-weight:600;margin-top:18px}
.mission p{font-size:11.5px;line-height:16px;margin-top:6px;color:#222}

.site-footer{position:absolute;left:0;top:2654px;width:1200px;height:219px;background:var(--footer);font-size:10px;color:#666}
.footer-nav{position:absolute;left:613px;top:49px;display:flex;gap:22px;color:#333}
.footer-rule{position:absolute;left:258px;width:678px;height:1px;background:#dcdce2}
.footer-col{position:absolute;line-height:17px}
.social{position:absolute;width:14px;height:14px;border:1.5px solid #777;border-radius:50%}
</style>
</head>
<body>

<header class="site-header">
  <div class="brand" style="left:170px;top:22px;font-size:17px"><span class="brand-dot"></span>Ebbtide Haven</div>
  <nav class="main-nav"><span>Home</span><span>Float</span><span>IR Sauna</span><span>mHBOT</span><span>Heat Mat</span><span>Gift Cards</span><span>Contact</span></nav>
  <div class="btn-book">BOOK APPOINTMENT</div>
</header>

<div class="hero" role="img" aria-label="Photo of a woman relaxing in a towel inside a wooden infrared sauna"></div>
<div class="blush-band"></div>
<div class="logo-badge">Ebbtide<br>Haven</div>

<div class="leaf-area" style="left:862px;top:860px;width:140px;height:70px;background:var(--leaf-pink)" role="img" aria-label="Soft pink leaf sprig decoration"></div>
<div class="leaf-area" style="left:135px;top:1255px;width:180px;height:90px;background:var(--leaf-lilac)" role="img" aria-label="Soft lilac leaf sprig decoration"></div>

<div class="photo" style="left:318px;top:650px;width:164px;height:127px;background:linear-gradient(135deg,#3a2f7a,#7a3df0 55%,#b07cff)" role="img" aria-label="Photo of a float pod glowing purple"></div>
<div class="photo" style="left:270px;top:764px;width:164px;height:159px;background:linear-gradient(160deg,#c9b9b2,#5c4e4a 60%,#2d2a2c)" role="img" aria-label="Photo of a woman floating in dark water"></div>
<div class="photo" style="left:450px;top:779px;width:131px;height:116px;background:linear-gradient(135deg,#d93fd6,#b840e8 55%,#58e3d8)" role="img" aria-label="Photo of a woman beside an open glowing float pod"></div>
<div class="abs service" style="left:627px;top:712px;width:286px">
  <div class="eyebrow">Body / Mind / Soul</div>
  <h2>Float</h2>
  <p>A floatation tank (float tank) is a dark, soundproof tank which is partially filled with salty water and is heated to outer skin temperature (approximately 35°C).</p>
  <div class="btn-dark">VIEW MORE</div>
</div>

<div class="abs service" style="left:264px;top:1055px;width:292px">
  <div class="eyebrow">Balance / Release / Restore</div>
  <h2>Infrared Sauna</h2>
  <p>Infrared Sauna or IR Sauna sessions usually involve sitting comfortably while infrared heaters directly heat your body. This is different to regular sauna’s that only heat the air around your body.</p>
  <div class="btn-dark">VIEW MORE</div>
</div>
<div class="photo" style="left:611px;top:977px;width:158px;height:253px;background:linear-gradient(160deg,#8a5a38,#d9cfc6 55%,#efe9e4)" role="img" aria-label="Photo of a smiling woman in a white robe in a sauna"></div>
<div class="photo" style="left:806px;top:991px;width:125px;height:169px;background:linear-gradient(160deg,#e0b98c,#d7a470 50%,#f1e3d6)" role="img" aria-label="Photo of a woman resting against sauna timber"></div>
<div class="photo" style="left:706px;top:1073px;width:97px;height:200px;background:linear-gradient(180deg,#b88550,#8c5b2e 60%,#6b3f1d)" role="img" aria-label="Photo of an infrared sauna cabin with glass door"></div>
<div class="photo" style="left:803px;top:1160px;width:81px;height:113px;background:linear-gradient(160deg,#a34a2a,#d65a3a 60%,#7a2d1a)" role="img" aria-label="Photo of an infrared sauna interior glowing red"></div>

<div class="abs benefits-title">Benefits of Floating</div>
<svg class="abs" style="left:285px;top:1355px" width="660" height="140" viewBox="0 0 660 140" aria-hidden="true">
  <path d="M2 100 C120 55 200 45 320 95 S520 125 600 75" fill="none" stroke="#e4e4ea" stroke-width="1"/>
  <path d="M597 32 L645 3 L632 52 L615 40 Z M615 40 L645 3 L620 52 L615 40" fill="none" stroke="#444" stroke-width="1.2" stroke-linejoin="round"/>
</svg>
<div class="benefit" style="left:265px;top:1397px">
  <div class="disc" style="background:var(--mental)"><svg width="56" height="56" viewBox="0 0 56 56" fill="none" stroke="#fff" stroke-width="2"><circle cx="28" cy="22" r="13"/><path d="M28 9v26M20 16c3 2 3 6 0 8M36 16c-3 2-3 6 0 8"/><path d="M8 30v12l10 8M48 30v12l-10 8"/></svg></div>
  <h3>Mental</h3>
  <p>Floating is an energizing, rejuvenating practice that improves health and well-being, alleviates stress, and facilitates meditation and self-improvement.</p>
</div>
<div class="benefit" style="left:499px;top:1397px">
  <div class="disc" style="background:var(--physical)"><svg width="60" height="60" viewBox="0 0 60 60" fill="none" stroke="#fff" stroke-width="2"><ellipse cx="30" cy="30" rx="26" ry="10"/><ellipse cx="30" cy="30" rx="26" ry="10" transform="rotate(60 30 30)"/><ellipse cx="30" cy="30" rx="26" ry="10" transform="rotate(-60 30 30)"/><circle cx="30" cy="30" r="4"/></svg></div>
  <h3>Physical</h3>
  <p>Floating helps eliminate fatigue and enter the flow state, improves sleep, speeds the body’s healing process, improves athletic performance and increases motivation.</p>
</div>
<div class="benefit" style="left:732px;top:1410px">
  <div class="disc" style="background:var(--creative)"><svg width="56" height="56" viewBox="0 0 56 56" fill="none" stroke="#fff" stroke-width="2"><circle cx="22" cy="24" r="9"/><path d="M18 33v5h8v-5M22 7v5M9 13l3 3M35 13l-3 3"/></svg></div>
  <h3 style="margin-top:7px">Creative</h3>
  <p>Floating facilitates creative insights, enhances problem-solving abilities, increases focus, expands awareness and accelerates learning.</p>
</div>

<div class="water" role="img" aria-label="Photo of a woman floating on calm blue water"></div>
<section class="booking-card">
  <h2>Book A Treatment</h2>
  <p class="lead">All bookings made online are pre-paid. An account is required to make an appointment online.</p>
  <div class="field" style="left:49px;top:116px;width:237px;height:29px">First Name</div>
  <div class="field" style="left:297px;top:116px;width:238px;height:29px">Email Address</div>
  <div class="field" style="left:49px;top:156px;width:237px;height:29px">Phone No</div>
  <div class="field" style="left:297px;top:156px;width:238px;height:29px">How did you hear about us?*</div>
  <div class="field" style="left:49px;top:196px;width:486px;height:57px">Message</div>
  <div class="btn-submit">BOOK NOW</div>
</section>

<div class="follow-line" style="left:256px;width:264px"></div>
<div class="follow-line" style="left:678px;width:261px"></div>
<div class="abs follow-label">FOLLOW US SNAPGRAM</div>
<div class="feed-tile" style="left:0;background:linear-gradient(160deg,#cbbdb8,#4a3f3c)" role="img" aria-label="Photo of a woman floating in dark water"></div>
<div class="feed-tile" style="left:199px;background:linear-gradient(160deg,#e3bb8c,#c98e5a)" role="img" aria-label="Photo of a woman resting in a timber sauna"></div>
<div class="feed-tile" style="left:401px;background:linear-gradient(160deg,#1c3fa8,#2c62d6)" role="img" aria-label="Photo of a woman floating in a blue-lit float room"></div>
<div class="feed-tile" style="left:602px;background:linear-gradient(160deg,#8a6a58,#d4b8a4)" role="img" aria-label="Photo of a woman receiving a massage by candlelight"></div>
<div class="feed-tile" style="left:803px;background:linear-gradient(160deg,#4fa0d8,#cfe6f2)" role="img" aria-label="Photo of a woman floating in bright water"></div>
<div class="feed-tile" style="left:1004px;background:linear-gradient(135deg,#d93fd6,#b840e8 55%,#58e3d8)" role="img" aria-label="Photo of a woman beside a glowing float pod"></div>

<section class="abs mission">
  <div class="dot"></div>
  <h2>Our Mission</h2>
  <p>Our mission is to provide a purpose-built space for our clients to relax, recover and optimise their health. Ebbtide Haven Spa offers Flotation Therapy, Mild Hyperbaric Oxygen Therapy (mHBOT), Infrared Sauna and Heat Mat sessions.</p>
</section>

<footer class="site-footer">
  <div class="brand" style="left:268px;top:37px;font-size:17px"><span class="brand-dot" style="width:34px;height:34px"></span>Ebbtide Haven</div>
  <nav class="footer-nav"><span>Home</span><span>Float</span><span>IR Sauna</span><span>mHBOT</span><span>Heat Mat</span><span>Gift Cards</span></nav>
  <div class="footer-rule" style="top:92px"></div>
  <div class="footer-col" style="left:259px;top:111px">Unit 4/218 Harbour Road, Kelsworth, QLD, 4512<br>admin@ebbtidehaven.com.au<br>1800 555 019</div>
  <div class="footer-col" style="left:718px;top:110px">Booking Policy<br>Membership Policy<br>Privacy Policy</div>
  <div class="footer-col" style="left:844px;top:109px">Cancellation Policy<br>FAQs<br>Sitemap</div>
  <div class="footer-col" style="left:258px;top:189px">© 2019 - EBBTIDE HAVEN</div>
  <div class="social" style="left:893px;top:190px"></div>
  <div class="social" style="left:918px;top:190px;border-radius:3px"></div>
</footer>

</body>
</html>
```